Business Card Design Project

Business card design for an IT Service company. A logo has already been created in a different contest and has been attached to this project. Ideally we're looking for a double sided business card that matches the look and feel of our newly created logo.

We're open to creativity if you feel a tag line is needed such as "IT Services and Application Development". We're open to really and look and feel - even single sided business cards if you feel you have something that's a great idea.

Last thought here - I'm not sure how it'll look but maybe a two tone card? One side dark blue and the other side white? Don't limit the design submissions to this tho - just curious if it would look good

Nothing too busy please - simple... Thank you and happy designing!

Target Market(s)

Businesses that require IT Services and support for hosted services, technical consultation, web design.

Industry/Entity Type

Business

Font styles to use
Sans Serif

Requirements
Must have
• Use the colors provided in the logo (see attachment) or additional colors that compliment
Must have the following contact info (not necessarily in this order):
- Alan Fisk
- Founding Partner
- afisk@quillbarrow.example
- 555-382-1946
- www.quillbarrow.example

```html
<!DOCTYPE html>
<html lang="en">
<head>
<meta charset="utf-8">
<title>Quillbarrow Business Card</title>
<link href="https://fonts.googleapis.com/css2?family=Roboto+Condensed:wght@300;400;700&display=swap" rel="stylesheet">
<style>
  :root {
    --page-bg: #ececef;
    --card-bg: #ffffff;
    --brand-navy: #14214a;
    --brand-green: #4f8a23;
    --ink: #111111;
  }
  * { margin: 0; padding: 0; box-sizing: border-box; }
  html, body {
    width: 1200px;
    height: 1000px;
    overflow: hidden;
    background: var(--page-bg);
    font-family: "Roboto Condensed", "Arial Narrow", sans-serif;
  }
  .card {
    position: absolute;
    left: 232px;
    top: 288px;
    width: 736px;
    height: 424px;
    background: var(--card-bg);
    border-radius: 18px;
  }
  .brand {
    position: absolute;
    left: 32px;
    top: 48px;
    display: flex;
    align-items: flex-end;
    gap: 20px;
    height: 116px;
  }
  .brand-square {
    width: 40px;
    height: 40px;
    background: var(--brand-green);
    margin-bottom: 8px;
  }
  .brand-name {
    font-size: 72px;
    font-weight: 700;
    color: var(--brand-navy);
    line-height: 1;
    letter-spacing: -0.5px;
  }
  .contact-block {
    position: absolute;
    right: 35px;
    top: 212px;
    text-align: right;
    color: var(--ink);
  }
  .person-name {
    font-size: 38px;
    font-weight: 300;
    line-height: 1.1;
  }
  .person-name .surname {
    font-weight: 700;
    margin-left: 16px;
  }
  .person-title {
    font-size: 22px;
    font-weight: 400;
    line-height: 1.2;
    margin-bottom: 34px;
  }
  .contact-line {
    font-size: 22px;
    font-weight: 400;
    line-height: 27px;
  }
</style>
</head>
<body>
  <div class="card">
    <div class="brand">
      <div class="brand-square"></div>
      <div class="brand-name">Quillbarrow</div>
    </div>
    <div class="contact-block">
      <div class="person-name">Alan<span class="surname">Fisk</span></div>
      <div class="person-title">Founding Partner</div>
      <div class="contact-line">afisk@quillbarrow.example</div>
      <div class="contact-line">555-382-1946</div>
      <div class="contact-line">www.quillbarrow.example</div>
    </div>
  </div>
</body>
</html>
```